Vehicle servicing digital billboard design

Needing a design to put on a digital billboard incorporating our brand/logo with website (lubebay.co.nz) phone number (09) 4817302 and our price offer (Full service from $79.95)

```html
<!DOCTYPE html>
<html lang="en">
<head>
<meta charset="utf-8">
<title>Lube Bay – Full service billboard</title>
<link rel="stylesheet" href="https://fonts.googleapis.com/css2?family=Fredoka:wght@600;700&display=swap">
<style>
  :root {
    --page-bg: #eeeeee;
    --brand-yellow: #ffc20e;
    --brand-orange: #f7941d;
    --panel-dark: #1c1c1c;
    --panel-dark-2: #2e2e2e;
    --silver-light: #f2f2f2;
    --silver-mid: #c9c9c9;
    --silver-dark: #9a9a9a;
    --ink: #141414;
    --headline: #e6e6e6;
  }
  html, body {
    margin: 0;
    padding: 0;
    width: 914px;
    height: 1200px;
    overflow: hidden;
    background: var(--page-bg);
  }
  .canvas {
    position: relative;
    width: 914px;
    height: 1200px;
  }
  .billboard {
    position: absolute;
    left: 20px;
    top: 381px;
    width: 874px;
    height: 437px;
    box-shadow: 0 6px 18px rgba(0,0,0,0.25);
  }
  .billboard svg { display: block; width: 100%; height: 100%; }
  .brand-name { font-family: "Fredoka", sans-serif; font-weight: 700; fill: var(--ink); }
  .headline { font-family: "Fredoka", sans-serif; font-weight: 700; fill: var(--headline); }
  .price {
    font-family: "Fredoka", sans-serif; font-weight: 700;
    fill: var(--brand-yellow); stroke: var(--silver-mid); stroke-width: 4; paint-order: stroke;
  }
  .contact { font-family: "Fredoka", sans-serif; font-weight: 700; fill: var(--ink); }
</style>
</head>
<body>
<main class="canvas">
  <section class="billboard" aria-label="Lube Bay full service offer billboard">
    <svg viewBox="0 0 1000 500" xmlns="http://www.w3.org/2000/svg">
      <defs>
        <radialGradient id="burst" cx="0.1" cy="0.3" r="1">
          <stop offset="0" stop-color="#ffd23a"/>
          <stop offset="0.6" stop-color="var(--brand-yellow)"/>
          <stop offset="1" stop-color="var(--brand-orange)"/>
        </radialGradient>
        <linearGradient id="dark" x1="0" y1="0" x2="1" y2="1">
          <stop offset="0" stop-color="var(--panel-dark-2)"/>
          <stop offset="1" stop-color="var(--panel-dark)"/>
        </linearGradient>
        <linearGradient id="silver" x1="0" y1="0" x2="1" y2="0">
          <stop offset="0" stop-color="var(--silver-dark)"/>
          <stop offset="0.45" stop-color="var(--silver-light)"/>
          <stop offset="1" stop-color="var(--silver-mid)"/>
        </linearGradient>
      </defs>

      <!-- dark offer panel -->
      <rect class="offer-panel" x="0" y="0" width="1000" height="500" fill="url(#dark)" role="img" aria-label="Dark honeycomb texture panel"/>

      <!-- yellow brand panel -->
      <polygon class="brand-panel" points="0,0 462,0 347,500 0,500" fill="url(#burst)" role="img" aria-label="Yellow and orange comic burst background"/>

      <!-- yellow accent stripe and silver contact band -->
      <polygon class="accent-stripe" points="372,382 1000,280 1000,298 368,398" fill="var(--brand-yellow)"/>
      <polygon class="contact-band" points="368,398 1000,298 1000,500 347,500" fill="url(#silver)"/>

      <!-- brand name -->
      <rect class="brand-mark" x="40" y="240" width="30" height="30" fill="var(--ink)"/>
      <text class="brand-name" x="84" y="270" font-size="46">Lube Bay</text>

      <!-- offer -->
      <text class="headline" x="712" y="96" font-size="56" text-anchor="middle">Full service from</text>
      <text class="price" x="715" y="250" font-size="150" text-anchor="middle" transform="skewX(-6) translate(25 0)">$79.95</text>

      <!-- contact -->
      <text class="contact" x="710" y="417" font-size="50" text-anchor="middle">(09) 4817302</text>
      <text class="contact" x="712" y="480" font-size="52" text-anchor="middle">lubebay.co.nz</text>
    </svg>
  </section>
</main>
</body>
</html>
```